lotus bowl vietnamese restaurant in need of a new menu

a family owned vietnamese restaurant in need of a new menu design that is fun, classy, and yet simple. menu that will catch the customers eyes. easy to read yet flows nicely. like to use the color green (basil green color) creme yellow and maroon. open to other colors as long as it looks nice together. our restaurant is family oriented, casual yet has a nice ambiance atmosphere.
prefer 11x17 portrait double sided. attached is our menu with the current price updated so use the info on this to start creating! looking for something unique, professional and one of a kind menu!
please use your own creative layout and design. we are open to ideas. the files uploaded are the updated prices and the logo is to use whichever one you feel goes with the menu.
Reason: don't see anything we like so far...please be creative!
Target Market(s)
restaurant consumers
Industry/Entity Type
Restaurant
Look and feel

```html
<!DOCTYPE html>
<html lang="en">
<head>
<meta charset="utf-8">
<title>Lotus Bowl – Take Out Menu</title>
<link rel="stylesheet" href="https://fonts.googleapis.com/css2?family=Lato:wght@400;700&family=Roboto+Condensed:wght@300;400;700&family=Alfa+Slab+One&display=swap">
<style>
  :root{
    --basil:#6cbf45;
    --basil-dark:#4f9a2e;
    --ink:#1e1e1e;
    --paper:#ffffff;
    --stage:#ebe8e3;
    --rule:#8a8a8a;
  }
  *{box-sizing:border-box;margin:0;padding:0}
  html,body{width:1200px;height:1200px;overflow:hidden;background:var(--stage)}
  .menu{
    position:absolute;left:20px;top:222px;width:1300px;height:847px;
    transform:scale(.8923);transform-origin:0 0;
    font-family:"Roboto Condensed",Arial,sans-serif;color:var(--ink);
    box-shadow:0 6px 18px rgba(0,0,0,.25);
  }
  .panel{position:absolute;top:0;height:847px;overflow:hidden}

  /* panel 1 */
  .panel--veg{left:0;width:438px;background:var(--basil)}
  .photo{position:absolute;border:2px solid var(--ink);border-radius:12px;overflow:hidden}
  .photo .tag{
    position:absolute;top:6px;width:26px;height:26px;border-radius:50%;
    background:var(--basil);color:var(--ink);font:700 11px/26px "Roboto Condensed",sans-serif;text-align:center;
  }
  .tag--l{left:6px}.tag--r{right:6px}
  .tag--bl{top:auto;bottom:6px;left:6px}.tag--br{top:auto;bottom:6px;right:6px}
  .g-soup{background:radial-gradient(circle at 50% 55%,#c9ad8a,#8c7560 60%,#d9d4cc)}
  .g-rice{background:radial-gradient(circle at 45% 50%,#efe7d8,#a5674a 65%,#e6e1d9)}
  .g-fish{background:radial-gradient(circle at 50% 50%,#d4653a,#5b2a1a 65%,#2a2220)}
  .g-beef{background:radial-gradient(circle at 50% 50%,#6d8b3e,#6a3b24 60%,#b9b1a6)}
  .g-shrimp{background:linear-gradient(135deg,#5e8d3a,#e79a6a 50%,#9bbf63)}
  .g-plate{background:radial-gradient(circle at 50% 50%,#b57a45,#d9c3a3 55%,#f4f1ec)}
  .g-seafood{background:linear-gradient(135deg,#c9c1b5,#e7b39b 45%,#8aa86a)}
  .g-pork{background:radial-gradient(circle at 50% 55%,#8f5a2f,#d8c7a4 60%,#f3efe7)}

  .veg-title{position:absolute;left:0;width:438px;top:302px;text-align:center;font:700 17px "Roboto Condensed",sans-serif;letter-spacing:.2px}
  .list{position:absolute;list-style:none;font-size:8.6px;line-height:13.3px;text-transform:uppercase}
  .list li{display:grid;grid-template-columns:22px 1fr}
  .list .num{grid-row:span 2}
  .list .line{display:flex;align-items:baseline}
  .list .line .lead{flex:1;border-bottom:1px dotted var(--ink);margin:0 2px;transform:translateY(-2px)}
  .list .desc{padding-left:2px}
  .list--veg{left:36px;top:338px;width:378px}
  .list--veg li{margin-bottom:0}

  /* panel 2 */
  .panel--drinks{left:438px;width:428px;background:var(--paper)}
  .drinks-photo{position:absolute;left:0;top:0;width:428px;height:300px;border-bottom-left-radius:55% 40%;border-bottom-right-radius:10% 20%;
    background:radial-gradient(circle at 55% 45%,#e9dfa8,#7d2a2a 35%,#55a84a 55%,#9d9a96 80%)}
  .badge{position:absolute;border-radius:50%;background:var(--ink);border:4px solid var(--paper);display:flex;align-items:center;justify-content:center;text-align:center}
  .badge--drinks{left:270px;top:180px;width:148px;height:148px;color:var(--basil);font:300 23px "Roboto Condensed",sans-serif}
  .list--drinks{left:18px;top:338px;width:382px}
  .flavors{display:grid;grid-template-columns:72px 72px 72px;padding-left:2px}
  .drinks-foot{position:absolute;left:0;bottom:0;width:428px;height:62px;background:var(--basil);
    font:italic 6.6px/9.8px "Roboto Condensed",sans-serif;text-align:center;padding-top:6px}

  /* panel 3 */
  .panel--cover{left:866px;width:434px;background:var(--basil)}
  .cover-top{position:absolute;left:0;top:0;width:434px;height:150px;background:var(--paper)}
  .cover-photo{position:absolute;left:0;top:145px;width:434px;height:580px;border-bottom-left-radius:45% 28%;
    background:radial-gradient(circle at 55% 45%,#f2efe4,#9fcf6b 40%,#4d8c2c 65%,#c94b45 92%)}
  .brand{position:absolute;left:0;top:92px;width:434px;text-align:center;font:700 46px "Lato",sans-serif;color:var(--ink);
    display:flex;justify-content:center;align-items:center;gap:14px}
  .brand .dot{width:14px;height:14px;border-radius:50%;background:var(--basil)}
  .pill{position:absolute;left:68px;top:172px;width:280px;height:36px;border-radius:18px;background:var(--basil);
    font:400 25px/36px "Lato",sans-serif;text-align:center;color:var(--ink)}
  .badge--takeout{left:13px;top:632px;width:150px;height:150px;color:var(--basil);font:26px/30px "Alfa Slab One",serif}
  .contact{position:absolute;right:20px;top:752px;text-align:right;font:400 21px/27px "Lato",sans-serif;color:var(--ink)}
</style>
</head>
<body>
<div class="menu">

  <section class="panel panel--veg">
    <div class="photo g-soup" style="left:28px;top:28px;width:196px;height:117px" role="img" aria-label="Seafood rice porridge in a bowl"><span class="tag tag--l">#10</span></div>
    <div class="photo g-rice" style="left:232px;top:28px;width:196px;height:117px" role="img" aria-label="Broken rice plate with pork chop and egg"><span class="tag tag--r">#45</span></div>
    <div class="photo g-fish" style="left:28px;top:155px;width:196px;height:117px" role="img" aria-label="Caramelised fish in clay pot"><span class="tag tag--bl">#41</span></div>
    <div class="photo g-beef" style="left:232px;top:155px;width:196px;height:117px" role="img" aria-label="Beef stew noodle bowl with herbs"><span class="tag tag--br">#40</span></div>

    <h2 class="veg-title">MON CHAY - VEGETARIAN PLATE</h2>
    <ol class="list list--veg">
      <li><span class="num">64.</span><span class="line">Goi Cuon Tofu<span class="lead"></span>4.50</span><span class="desc">Fried tofu spring roll</span></li>
      <li><span class="num">65.</span><span class="line">Soup Rau Cai<span class="lead"></span>(S) | 3.00 &nbsp;(L) | 5.95</span><span class="desc">Vegetables soup</span></li>
      <li><span class="num">66.</span><span class="line">Pho Dau Hu Rau Cai<span class="lead"></span>9.50</span><span class="desc">Fried tofu &amp; vegetables noodle soup</span></li>
      <li><span class="num">67.</span><span class="line">Dau Hu Xao Rau Cai<span class="lead"></span>9.95</span><span class="desc">Stir fry tofu with mixed vegetables</span></li>
      <li><span class="num">68.</span><span class="line">Dau Hu Xao Xa Ot<span class="lead"></span>9.95</span><span class="desc">Stir fry fried tofu with hot chilli &amp; lemongrass</span></li>
      <li><span class="num">69.</span><span class="line">Bun Xao Dau Hu Rau Cai<span class="lead"></span>9.50</span><span class="desc">Stir fry vermecelli with fried tofu &amp; mixed vegetables</span></li>
      <li><span class="num">70</span><span class="line">Com Chien Dau Hu Rau Cai<span class="lead"></span>9.50</span><span class="desc">Fried tofu &amp; vegetables fried rice</span></li>
      <li><span class="num">71</span><span class="line">Bun Dau Hu<span class="lead"></span>9.25</span><span class="desc">Fried tofu vermicelli bowl</span></li>
    </ol>

    <div class="photo g-shrimp" style="left:28px;top:580px;width:196px;height:116px" role="img" aria-label="Shrimp salad with herbs"><span class="tag tag--l">#37</span></div>
    <div class="photo g-plate" style="left:232px;top:580px;width:196px;height:116px" role="img" aria-label="Fried rice with grilled meat"><span class="tag tag--r">#53</span></div>
    <div class="photo g-seafood" style="left:28px;top:706px;width:196px;height:116px" role="img" aria-label="Seafood noodle soup"><span class="tag tag--l">#12</span></div>
    <div class="photo g-pork" style="left:232px;top:706px;width:196px;height:116px" role="img" aria-label="Grilled pork with rice and salad"><span class="tag tag--r">#44</span></div>
  </section>

  <section class="panel panel--drinks">
    <div class="drinks-photo" role="img" aria-label="Layered three colour dessert drink with bowls of beans and jelly"></div>
    <div class="badge badge--drinks">BEVERAGES</div>
    <ol class="list list--drinks">
      <li><span class="num">72</span><span class="line">Nuoc Ngot - Soda<span class="lead"></span>1.50</span><span class="desc">Fizz Cola • Diet Fizz • Fizz Zero • Blue Pop • Peak Citrus • Sunny Orange • Spice Soda •<br>Lime Spark • Club Soda • Gingerale • Oak Barrel Rootbeer • Bottle Water</span></li>
      <li><span class="num">73</span><span class="line">Nuoc Dua<span class="lead"></span>4.25</span><span class="desc">Fresh coconut juice</span></li>
      <li><span class="num">74</span><span class="line">Cam Vat<span class="lead"></span>4.00</span><span class="desc">Fresh orange juice</span></li>
      <li><span class="num">75</span><span class="line">Da Chanh<span class="lead"></span>3.50</span><span class="desc">Fresh limeade juice</span></li>
      <li><span class="num">76</span><span class="line">Soda Da Chanh<span class="lead"></span>4.00</span><span class="desc">Fresh limeade with club soda</span></li>
      <li><span class="num">77</span><span class="line">Thai Ice Tea<span class="lead"></span>4.00</span><span class="desc">Thai tea mix with half &amp; half milk</span></li>
      <li><span class="num">78</span><span class="line">Clearspring Sparking Mineral Water<span class="lead"></span>1.95</span></li>
      <li><span class="num">79</span><span class="line">Cafe Sua Da or Den Da<span class="lead"></span>3.50</span><span class="desc">Vietnamese milk ice coffee or black coffee (hot or cold)</span></li>
      <li><span class="num">80</span><span class="line">Chanh Muoi<span class="lead"></span>3.50</span><span class="desc">Salty brined lime juice</span></li>
      <li><span class="num">81</span><span class="line">Soda Chanh Muoi<span class="lead"></span>4.25</span><span class="desc">Salty brined lime juice with club soda</span></li>
      <li><span class="num">82</span><span class="line">Sua Hot Ga<span class="lead"></span>4.25</span><span class="desc">Sweet milk &amp; egg with club soda</span></li>
      <li><span class="num">83</span><span class="line">Sau Dau Nanh<span class="lead"></span>3.00</span><span class="desc">Soy bean milk</span></li>
      <li><span class="num">84</span><span class="line">Tra Da<span class="lead"></span>1.50</span><span class="desc">Unsweetened ice tea</span></li>
      <li><span class="num">85</span><span class="line">Che 3 Mau<span class="lead"></span>3.50</span><span class="desc">Vietnamese 3 color dessert</span></li>
      <li><span class="num">86</span><span class="line">Sinh To - Pearl Smoothies<span class="lead"></span>4.50</span>
        <span class="flavors"><span>Avocado</span><span>Banana</span><span>Coconut</span><span>Durian</span><span>Honeydew</span><span>Green Tea</span><span>Strawberry</span><span>Taro</span><span>Thai Tea</span></span></li>
      <li><span class="num"></span><span class="line">*Extra Pearls<span class="lead"></span>.75</span></li>
    </ol>
    <p class="drinks-foot">* Menu and prices are subject to change without notice. | No substituting food item/s on any entrees.<br>** Consuming raw or undercooked meats, poultry, seafood, shellfish, eggs or<br>unpasteurized milk may increase your risk of foodborne illness.<br>*** Please alert your server for any food allergies/intolerance before ordering.</p>
  </section>

  <section class="panel panel--cover">
    <div class="cover-photo" role="img" aria-label="Noodle soup bowl topped with herbs, bean sprouts, chilli and lime"></div>
    <div class="cover-top"></div>
    <h1 class="brand">Lotus <span class="dot"></span> Bowl</h1>
    <p class="pill">Vietnamese Restaurant</p>
    <div class="badge badge--takeout">TAKE<br>OUT<br>MENU</div>
    <address class="contact" style="font-style:normal">(555) 310-2748<br>1280 Willow Bend Ave<br>Maple Grove, FL 33000</address>
  </section>

</div>
</body>
</html>
```